Childrens Development/Fun Centre needs a Kid-Centric website

We need a website devoted to what we love, children, this site should be similar to other children development centre website which offer similar services and developments (best example - m o s s y p e r c h . c o . u k)

We need to reflect our values of being fun and friendly whilst also imparting important skills and knowledge onto children. The website should have a button at the top for login (we are using the same MIS system as the example website listed above - so the login and members pages will be hosted by a third party site).

The site should incorporate a like us on chatterdeck button, a snapwheel feed (please only use cobalt framedeck plugin for the snapwheel, for the quibbly you can just use the standard code from quibbly no need for a plugin)

We need to have postwren on the site too with a form to join our mailing list.

Initially we want to see some nice designs which are similar in feel and vibe of the logo which is enclosed, in a format the same as the example listed above.

thanks

Reason: Hi, Apologies for the delay and the miscommunication, we need this website actually CODED, the design can be directly based on the design of the website mentioned in the brief. please only submit or send me a message if your proposal was for CODING! thanks

```html
<!DOCTYPE html>
<html lang="en">
<head>
<meta charset="utf-8">
<title>Tumble Nest</title>
<link href="https://fonts.googleapis.com/css2?family=Open+Sans:ital,wght@0,400;0,600;0,700;1,400&family=Ubuntu:wght@400;500;700&family=Delius+Swash+Caps&display=swap" rel="stylesheet">
<style>
:root{
  --lime:#8fc043;
  --lime-light:#c5dc52;
  --lime-pale:#e6efb8;
  --forest:#1f6b2e;
  --forest-dark:#17571f;
  --ink:#555;
  --muted:#777;
  --panel:#f4f4f4;
  --mint:#c6f1de;
  --sky:#9fe0d8;
  --purple:#4f4a8a;
}
*{box-sizing:border-box;margin:0;padding:0}
html,body{width:768px;height:1200px;overflow:hidden}
body{position:relative;font-family:"Open Sans",sans-serif;color:var(--ink);
  background:linear-gradient(180deg,#e9fbf2 0%,var(--mint) 35%,#b9ecd7 70%,var(--sky) 100%)}
.abs{position:absolute}
.topbar{left:0;top:0;width:768px;height:5px;background:var(--purple)}
.brand{left:86px;top:28px;font-family:"Ubuntu",sans-serif;font-weight:700;font-size:34px;color:var(--forest);letter-spacing:.5px;white-space:nowrap}
.brand-dot{left:300px;top:34px;width:16px;height:16px;border-radius:50%;background:var(--lime)}
.social{left:526px;top:14px;display:flex;gap:5px}
.social span{width:28px;height:28px;border-radius:50%;background:#ecd9b4;display:block}
.search{left:484px;top:61px;width:200px;height:23px;background:var(--lime-light);color:#fff;font-size:10px;padding:5px 7px}
.search svg{position:absolute;right:6px;top:5px}
.nav-cap{left:72px;top:100px;width:624px;height:16px;background:var(--lime);clip-path:polygon(2% 0,98% 0,100% 100%,0 100%)}
.nav{left:72px;top:116px;width:624px;height:36px;background:#fff}
.nav a{position:absolute;top:8px;height:20px;border-radius:10px;background:var(--lime-light);color:var(--forest);font-size:9px;text-decoration:none;text-align:center;line-height:20px}
.slider{left:84px;top:152px;width:600px;height:266px;background:var(--lime)}
.slider-frame{left:96px;top:166px;width:578px;height:232px;border:3px solid var(--lime-pale);border-radius:4px;background:#f7f7f1}
.slide-photo{left:110px;top:180px;width:552px;height:206px;background:linear-gradient(90deg,#e7b48e 0%,#f1d2b8 40%,#f3efe6 62%,#eef0e8 100%)}
.slide-copy{left:330px;top:206px;width:312px;text-align:right;color:var(--forest)}
.slide-copy h2{font-family:"Ubuntu",sans-serif;font-weight:400;font-size:19px;line-height:24px}
.slide-copy h2 b{font-weight:700;font-size:23px}
.slide-copy p{font-size:9.5px;line-height:20.4px;margin-top:4px}
.btn-more{left:550px;top:344px;width:92px;height:26px;background:var(--lime-light);color:var(--forest);font-size:9.5px;text-align:center;line-height:26px}
.dots{left:338px;top:381px;width:103px;height:17px;background:var(--forest);display:flex;gap:4px;justify-content:center;align-items:center}
.dots i{width:6px;height:6px;border-radius:50%;background:#fff;display:block}
.dots i:first-child{background:var(--forest);border:1.5px solid #fff}
.ribbon{top:392px;width:24px;height:10px;background:var(--forest-dark)}
.panel{left:84px;top:438px;width:600px;height:722px;background:var(--panel)}
.welcome{left:84px;top:449px;width:600px;text-align:center;color:var(--forest);font-size:10px;font-weight:700}
.welcome span{font-family:"Delius Swash Caps",cursive;font-weight:400;font-size:15px}
.intro{left:118px;top:480px;width:532px;text-align:center;font-size:8.6px;line-height:20.4px;color:var(--muted)}
.intro-join{left:118px;top:590px;width:532px;text-align:center;font-size:8.6px;color:var(--muted)}
.script{font-family:"Delius Swash Caps",cursive;font-weight:400;color:var(--forest);text-transform:uppercase;white-space:nowrap}
.h-news{left:94px;top:643px;font-size:13.5px}
.h-say{left:552px;top:646px;font-size:10.5px}
.news{top:672px;width:132px;text-align:center}
.news .ph{height:80px;border-radius:2px}
.news h3{font-family:"Delius Swash Caps",cursive;font-weight:400;font-size:10px;color:var(--forest);text-transform:uppercase;margin-top:8px;white-space:nowrap}
.news .date{font-style:italic;font-size:8.5px;color:var(--muted);margin-top:3px}
.news p{font-size:8.5px;line-height:13.3px;color:var(--ink);margin-top:3px}
.quote{left:554px;top:672px;width:113px;height:108px;background:var(--forest);color:#fff;font-family:"Delius Swash Caps",cursive;font-size:8.5px;line-height:13.8px;text-align:center;padding-top:8px;text-transform:uppercase}
.author{left:558px;top:793px;font-size:8.5px;color:var(--ink);display:flex;align-items:center;gap:5px;white-space:nowrap}
.author b{font-family:"Delius Swash Caps",cursive;font-weight:400;color:var(--forest);font-size:7.5px;text-transform:uppercase}
.h-tw{left:94px;top:883px;font-size:10px}
.follow{left:192px;top:882px;width:80px;height:12px;border:1px solid #ccc;border-radius:2px;background:#f9f9f9;font-size:6.5px;font-weight:700;color:#333;padding-left:3px;line-height:10px;white-space:nowrap;overflow:hidden}
.follow::before{content:"";display:inline-block;width:5px;height:5px;border-radius:50%;background:#2ea1de;margin-right:2px}
.tweet{left:93px;width:180px;display:flex;gap:7px;border-bottom:1px solid #ddd;padding-bottom:9px}
.tweet .av{width:38px;height:36px;flex:none}
.tweet p{font-family:Arial,sans-serif;font-size:6.8px;line-height:8.6px;color:#333;text-align:justify}
.tweet b,.tweet em{color:#2ea1de;font-style:normal}
.fb{left:298px;top:883px;width:174px;height:189px;background:#fff;border:1px solid #ddd;padding:8px 14px}
.fb-head{display:flex;gap:7px}
.fb-badge{width:26px;height:26px;border:1px solid #888;border-radius:50%}
.fb-name{font-size:8.5px;font-weight:700;color:#3b5998}
.fb-name small{font-weight:400;font-size:6.5px}
.fb-like{margin-top:3px;width:28px;height:11px;border:1px solid #aaa;border-radius:2px;font-size:6px;color:#3b5998;text-align:center;line-height:9px}
.fb-count{margin-top:10px;border-top:1px solid #ddd;padding-top:6px;font-size:6.5px;color:#333}
.fb-grid{display:grid;grid-template-columns:repeat(4,31px);column-gap:4px;row-gap:6px;margin-top:6px}
.fb-grid div{font-size:5.5px;color:#777;text-align:center}
.fb-grid span{display:block;height:31px;margin-bottom:3px}
.fb-foot{position:absolute;left:14px;bottom:6px;font-size:5.8px;color:#3b5998;border-top:1px solid #ddd;width:146px;padding-top:3px}
.insta{left:496px;top:883px;width:164px;height:189px;background:#fafaf5;border:1px solid #e5e5e5}
.insta h4{position:absolute;left:13px;top:10px;font-family:"Delius Swash Caps",cursive;font-weight:400;font-size:10.5px;color:var(--forest);text-transform:uppercase;white-space:nowrap}
.insta-grid{position:absolute;left:4px;top:31px;display:grid;grid-template-columns:repeat(3,48px);gap:5px}
.insta-grid span{height:48px;display:block}
.mailing{left:153px;top:1091px;width:428px;height:59px;background:var(--lime-light)}
.mailing h4{position:absolute;left:11px;top:20px;font-family:"Delius Swash Caps",cursive;font-weight:400;font-size:12.5px;color:var(--forest);text-transform:uppercase;white-space:nowrap}
.mailing .field{position:absolute;left:171px;top:20px;width:154px;height:23px;background:#fff;font-size:7.5px;color:#333;padding:6px}
.mailing .join{position:absolute;left:343px;top:21px;width:62px;height:21px;background:var(--forest);color:#fff;font-family:"Delius Swash Caps",cursive;font-size:8.5px;text-align:center;line-height:21px;text-transform:uppercase}
.footer{left:84px;top:1160px;width:600px;height:40px;background:var(--lime);color:#fff;font-size:8.5px;text-align:center;line-height:40px}
</style>
</head>
<body>
<div class="abs topbar"></div>

<header>
  <div class="abs brand">Tumble Nest</div>
  <div class="abs brand-dot"></div>
  <div class="abs social" aria-label="Social links">
    <span title="chatterdeck"></span><span title="circlepost"></span><span title="snapwheel"></span><span title="quibbly"></span><span title="reeltube"></span>
  </div>
  <div class="abs search">Search.....
    <svg width="12" height="12" viewBox="0 0 12 12"><circle cx="5" cy="5" r="3.5" fill="none" stroke="#1f6b2e" stroke-width="1.8"/><line x1="7.6" y1="7.6" x2="11" y2="11" stroke="#1f6b2e" stroke-width="2"/></svg>
  </div>
  <div class="abs nav-cap"></div>
  <nav class="abs nav">
    <a style="left:33px;width:68px">Home</a>
    <a style="left:128px;width:68px">careers</a>
    <a style="left:229px;width:67px">About Us</a>
    <a style="left:325px;width:68px">Reference</a>
    <a style="left:417px;width:87px">Testimonial</a>
    <a style="left:529px;width:67px">contact us</a>
  </nav>
</header>

<section>
  <div class="abs slider"></div>
  <div class="abs slider-frame"></div>
  <div class="abs slide-photo" role="img" aria-label="Smiling child holding up a paint-covered hand, with children playing in the background"></div>
  <div class="abs slide-copy">
    <h2><b>JOIN ONLINE</b> TODAY AS<br>A MONTHLY</h2>
    <p>cancel and reschedule classes with ease using<br>our smart phone App and online booking<br>system. No more costly termly payments and<br>lost sessions.</p>
  </div>
  <div class="abs btn-more">READ MORE</div>
  <div class="abs ribbon" style="left:316px;clip-path:polygon(0 50%,100% 0,100% 100%)"></div>
  <div class="abs ribbon" style="left:439px;clip-path:polygon(0 0,100% 50%,0 100%)"></div>
  <div class="abs dots"><i></i><i></i><i></i><i></i><i></i></div>
</section>

<main>
  <div class="abs panel"></div>
  <h1 class="abs welcome">WELCOME TO <span>Tumble Nest</span></h1>
  <p class="abs intro">Established in 2011. we've transformed the traditional mum &amp; baby group with our innovative new approach. Our members enjoy fabulous classes, talks and events all wrapped up under one 'mossyperch' umbrella. Our signature classes take place in lovely family friendly venues in Ashcombe, Fernley &amp; Wexham and our teachers are the best in the business and qualified for your peace of mind. We give you the flexibility to book, cancel and reschedule classes with ease using our smart phone App and online booking system. No more costly termly payments and lost sessions.</p>
  <p class="abs intro-join">Join online today as a monthly or pay as you go member and find out why so many mums LOVE mossyperch!</p>

  <h2 class="abs script h-news">Latest News</h2>
  <h2 class="abs script h-say">What members say</h2>

  <article class="abs news" style="left:92px">
    <div class="ph" role="img" aria-label="Children at a birthday party with balloons and presents" style="background:linear-gradient(135deg,#f4a24a,#e2553f 55%,#79b6e0)"></div>
    <h3>Team Tumble Nest!</h3>
    <div class="date">June 2nd, 2014</div>
    <p>Well done team mossyperch<br>On the 1st June 2014 a team of 8<br>Fernley mossyperch [...]</p>
  </article>
  <article class="abs news" style="left:244px">
    <div class="ph" role="img" aria-label="Children eating watermelon on the beach" style="background:linear-gradient(135deg,#e9c9a0,#e46d6a 55%,#c9d8e6)"></div>
    <h3>Children Develop</h3>
    <div class="date">June 2nd, 2014</div>
    <p>Well done team mossyperch<br>On the 1st June 2014 a team of 8<br>Fernley mossyperch [...]</p>
  </article>
  <article class="abs news" style="left:396px">
    <div class="ph" role="img" aria-label="Children lying on the grass in a sunny park" style="background:linear-gradient(135deg,#8fb54a,#d7d83d 55%,#6a9a33)"></div>
    <h3>Fun Center</h3>
    <div class="date">June 2nd, 2014</div>
    <p>Well done team mossyperch<br>On the 1st June 2014 a team of 8<br>Fernley mossyperch [...]</p>
  </article>

  <blockquote class="abs quote">Mabel<br>absolutely<br>loves Wren.<br>Mini dancers is<br>the highlight<br>of our week!</blockquote>
  <div class="abs author">
    <svg width="14" height="14" viewBox="0 0 14 14"><circle cx="7" cy="4" r="3.2" fill="#1f6b2e"/><path d="M1 14c0-4 2.7-6 6-6s6 2 6 6z" fill="#1f6b2e"/></svg>
    <span><b>Hattie Clowes</b>, Ashcombe</span>
  </div>

  <h2 class="abs script h-tw">quibbly feeds</h2>
  <div class="abs follow">Follow @orlapenning</div>
  <div class="abs tweet" style="top:914px">
    <div class="av" role="img" aria-label="Grandparents photo" style="background:linear-gradient(135deg,#8fb1d6,#e6c1a0)"></div>
    <p><b>@ Orla Penning</b> The core ideas around distributed digital preservation are well-recognized in the library and... <em>qb.ly/s7RTN-418</em> 1 week ago</p>
  </div>
  <div class="abs tweet" style="top:972px">
    <div class="av" role="img" aria-label="Group of children photo" style="background:linear-gradient(135deg,#f2e3d0,#8bc27a)"></div>
    <p><b>@ Orla Penning</b> The core ideas around distributed digital preservation are well-recognized in the library and... <em>qb.ly/s7RTN-418</em> 1 week ago</p>
  </div>
  <div class="abs tweet" style="top:1026px">
    <div class="av" role="img" aria-label="Children in a park photo" style="background:linear-gradient(135deg,#e9d34a,#6f9a3d)"></div>
    <p><b>@ Orla Penning</b> The core ideas around distributed digital preservation are well-recognized in the library and... <em>qb.ly/s7RTN-418</em> 1 week ago</p>
  </div>

  <div class="abs fb">
    <div class="fb-head">
      <div class="fb-badge"></div>
      <div>
        <div class="fb-name">Maple Rooms <small>on chatterdeck</small></div>
        <div class="fb-like">Like</div>
      </div>
    </div>
    <div class="fb-count">39 people like <b>Maple Rooms</b>.</div>
    <div class="fb-grid">
      <div><span role="img" aria-label="Member photo" style="background:#b8533f"></span>Ned</div>
      <div><span role="img" aria-label="Member photo" style="background:#d98b5c"></span>Katrin</div>
      <div><span role="img" aria-label="Member photo" style="background:#4a4a4a"></span>Shona</div>
      <div><span role="img" aria-label="Member photo" style="background:#7a5a4a"></span>Bea</div>
      <div><span role="img" aria-label="Member photo" style="background:#2e4f7a"></span>Cora</div>
      <div><span role="img" aria-label="Member photo" style="background:#8a7a6a"></span>Gina</div>
      <div><span role="img" aria-label="Member photo" style="background:#9fb6c8"></span>Shelly</div>
      <div><span role="img" aria-label="Member photo" style="background:#6d6d6d"></span>Stan</div>
    </div>
    <div class="fb-foot">chatterdeck social plugin</div>
  </div>

  <div class="abs insta">
    <h4>snapwheel feed</h4>
    <div class="insta-grid">
      <span role="img" aria-label="Child photo" style="background:#e8d6c6"></span>
      <span role="img" aria-label="Family photo" style="background:#c88a78"></span>
      <span role="img" aria-label="Children outdoors photo" style="background:#9ec3d9"></span>
      <span role="img" aria-label="Child jumping photo" style="background:#3f8fc6"></span>
      <span role="img" aria-label="Children in autumn photo" style="background:#d7b36a"></span>
      <span role="img" aria-label="Children reading photo" style="background:#a3503f"></span>
      <span role="img" aria-label="Children in the grass photo" style="background:#92b457"></span>
      <span role="img" aria-label="Child in a sun hat photo" style="background:#5cc2c6"></span>
      <span role="img" aria-label="Children smiling photo" style="background:#e9b3b0"></span>
    </div>
  </div>

  <form class="abs mailing">
    <h4>Join our mailing</h4>
    <div class="field">Enter ur mail id...</div>
    <div class="join">Join us</div>
  </form>
</main>

<footer class="abs footer">Copyright © 2013-2014 TUMBLE NEST. All rights reserved.</footer>
</body>
</html>
```